Business branding (card, web design) needed for Remedial / Sports massage

I need a clean, fresh design for my sports massage business called Swiftmoor-Core.

I work with high profile professional sports teams (massage, clinical tapeing, health assessments, pilates, coaching) however would like to expand into the entertainment market so need a design that would appeal to both.
NO LOTUS FLOWERS, HANDS OR YOGA POSES FOR DESIGNS

The successful brand design will need to be scalable (e.g. resolution/sizing) to work holistically across my website, marketing collateral and clothing.

Colour pallets that appeal to me - Black, white, blue, green, taupe,
and would prefer clean crisp designs that evoke professionalism, continuous improvement, flow and balance.

Good Luck, can't wait to find my new brand... :)
Updates

I have uploaded a business card that I do like,  See if you can be creative with the logo

Thanks

Target Market(s)

professional sports teams / athletes, and entertainment professionals.

I HAVE UPLOADED A PDF OF WHAT I HAVE DONE. YOU MAY USE LOGO BUT BE CREATIVE PLEASE.

Industry/Entity Type

Entertainment

Contact Information for Business Card

Swiftmoor-Core
'Recover Faster' (strap line)

Carla Wendover
Director / Remedial Massage

0471382605
612 Brisley Street
Hampton, VIC 3188

www.swiftmoor-core.com.au
info@swiftmoor-core.com.au

Logo Text

Swiftmoor-Core

Logo styles of interest
Pictorial/Combination Logo
Abstract Logo
Requirements
Should not have
• FLOWERS

```html
<!DOCTYPE html>
<html lang="en">
<head>
<meta charset="utf-8">
<title>Swiftmoor-Core — Business Card</title>
<link href="https://fonts.googleapis.com/css2?family=Arimo&family=Handlee&display=swap" rel="stylesheet">
<style>
  :root {
    --paper: #ffffff;
    --ink: #111111;
    --accent-red: #e8202a;
    --accent-green: #c4d42e;
    --accent-indigo: #4a4fa0;
    --accent-sky: #7dcff0;
    --mark-grey: #e6e7e9;
    --backdrop-grey: #f3f3f4;
  }
  html, body {
    margin: 0;
    padding: 0;
    width: 1200px;
    height: 686px;
    overflow: hidden;
    background: var(--paper);
  }
  .card {
    position: relative;
    width: 1200px;
    height: 686px;
    background: var(--paper);
    overflow: hidden;
    font-family: "Arimo", Arial, sans-serif;
  }
  .backdrop-circle {
    position: absolute;
    left: 526px;
    top: 6px;
    width: 846px;
    height: 846px;
    border-radius: 50%;
    background: var(--backdrop-grey);
  }
  .brand-dot {
    position: absolute;
    left: 114px;
    top: 97px;
    width: 206px;
    height: 206px;
    border-radius: 50%;
    background: var(--mark-grey);
  }
  .brand-name {
    position: absolute;
    left: 80px;
    top: 327px;
    margin: 0;
    font-size: 43px;
    line-height: 43px;
    font-weight: 400;
    color: var(--ink);
  }
  .brand-tagline {
    position: absolute;
    left: 90px;
    top: 378px;
    margin: 0;
    font-family: "Handlee", cursive;
    font-size: 29px;
    line-height: 36px;
    color: var(--accent-sky);
  }
  .person-name {
    position: absolute;
    right: 86px;
    top: 96px;
    margin: 0;
    font-size: 73px;
    line-height: 73px;
    font-weight: 400;
    color: var(--ink);
  }
  .person-role {
    position: absolute;
    right: 86px;
    top: 193px;
    margin: 0;
    font-size: 43px;
    line-height: 43px;
    color: var(--accent-red);
  }
  .address {
    position: absolute;
    left: 80px;
    top: 479px;
    margin: 0;
    font-style: normal;
    font-size: 32px;
    line-height: 40px;
    color: var(--accent-green);
  }
  .contact {
    position: absolute;
    right: 78px;
    top: 469px;
    margin: 0;
    padding: 0;
    list-style: none;
    text-align: right;
    font-size: 30px;
    line-height: 40px;
    color: var(--accent-indigo);
  }
</style>
</head>
<body>
  <main class="card">
    <div class="backdrop-circle" aria-hidden="true"></div>

    <div class="brand-dot" aria-hidden="true"></div>
    <p class="brand-name">Swiftmoor-Core</p>
    <p class="brand-tagline">‘Recover Faster’</p>

    <h1 class="person-name">Carla Wendover</h1>
    <p class="person-role">Remedial Massage Therapist</p>

    <address class="address">
      612 Brisley Street<br>
      Hampton<br>
      Vic 3188
    </address>

    <ul class="contact">
      <li>0471382605</li>
      <li>info@swiftmoor-core.com.au</li>
      <li>www.swiftmoor-core.com.au</li>
    </ul>
  </main>
</body>
</html>
```